Business Cards for Branding (Advertising) Agency

We need stylish and cool business cards.
Additional info:
1) Logo - see the attachment. You can use either the three penguins or just one penguin face (square or round) - at your discretion.
2) Text and other stuff for business card:
front side:
-Logo and company name: company name - Coastal Herons - should be in English as is in logo. This is the only exception. The rest of the text will be in Russian.
-Who we are: Брендинговое агентство
-First and last name:
-Position: Управляющий партнёр
-Address:
-Phone:
-Email:
-Website:
Note: please don't use names of information fields, such as: who we are, first and last name, position, address, phone, email and website.

3) Our suggestions on design:
-The backside of the business card can be either blank or has something on it - at your discretion.
-The business card background should be either white or grey (you can use any tone of grey).

Additional Information:
1) БРЕНДИНГОВОЕ АГЕНТСТВО
2) ул. Вересковая - these two words should be together on the same line
3) тел.: +7 (495) 381-62-09
моб.: +7 (916) 740-28-51

Reason: We would like to receive more stylish designs.

```html
<!DOCTYPE html>
<html lang="ru">
<head>
<meta charset="utf-8">
<title>Coastal Herons — визитка</title>
<link rel="stylesheet" href="https://fonts.googleapis.com/css2?family=PT+Serif&family=Arimo&display=swap">
<style>
  :root {
    --stage: #000000;
    --card: #ffffff;
    --frame: #cfd8d5;
    --ink-serif: #8e9b99;
    --ink-sans: #8f9897;
    --ink-brand: #1e1e1e;
    --ink-web: #8a8a8a;
    --mark-top: #3a3a3a;
    --mark-bottom: #111111;
  }
  html, body {
    margin: 0;
    padding: 0;
    width: 1200px;
    height: 900px;
    overflow: hidden;
    background: var(--stage);
  }
  .card {
    position: absolute;
    left: 44px;
    top: 32px;
    width: 1120px;
    height: 670px;
    background: var(--card);
  }
  .card__frame {
    position: absolute;
    left: 20px;
    top: 12px;
    width: 1060px;
    height: 626px;
    border: 11px solid var(--frame);
  }
  .brand__mark {
    position: absolute;
    left: 180px;
    top: 90px;
    width: 230px;
    height: 230px;
    border-radius: 50%;
    background: linear-gradient(180deg, var(--mark-top), var(--mark-bottom));
  }
  .brand__name {
    position: absolute;
    left: 60px;
    top: 352px;
    width: 470px;
    text-align: center;
    font-family: "PT Serif", serif;
    font-size: 52px;
    line-height: 1;
    letter-spacing: 3px;
    color: var(--ink-brand);
    white-space: nowrap;
  }
  .brand__web {
    position: absolute;
    left: 80px;
    top: 448px;
    width: 430px;
    text-align: center;
    font-family: "Arimo", Arial, sans-serif;
    font-size: 20px;
    color: var(--ink-web);
  }
  .identity {
    position: absolute;
    left: 496px;
    top: 124px;
    width: 590px;
    text-align: center;
    font-family: "PT Serif", serif;
    font-size: 44px;
    color: var(--ink-serif);
    line-height: 1;
  }
  .identity p { margin: 0 0 43px; }
  .contacts {
    position: absolute;
    right: 54px;
    top: 519px;
    text-align: right;
    font-family: "Arimo", Arial, sans-serif;
    font-size: 23px;
    letter-spacing: 0.3px;
    color: var(--ink-sans);
    line-height: 1;
  }
  .contacts p { margin: 0 0 18px; }
  .contacts .contacts__email { margin-top: 27px; }
</style>
</head>
<body>
  <div class="card">
    <div class="card__frame"></div>

    <div class="brand__mark" role="img" aria-label="Место для знака агентства"></div>
    <div class="brand__name">Coastal Herons</div>
    <div class="brand__web">www.coastalherons.ru</div>

    <div class="identity">
      <p class="identity__what">Брендинговое агентство</p>
      <p class="identity__name">Мария Ветрова</p>
      <p class="identity__role">Управляющий партнёр</p>
    </div>

    <div class="contacts">
      <p class="contacts__address">117105, г. Москва, ул. Вересковая, д.12, стр.2</p>
      <p class="contacts__phone">+7 (916) 740-28-51</p>
      <p class="contacts__email">maria@coastalherons.ru</p>
    </div>
  </div>
</body>
</html>
```